YouTube Banner for Psychologist
LiviaNotes
Project: YouTube Banner for Psychologist
Creative Brief
I'm a licensed clinical psychologist with extensive experience. My clients often say "Well Livia Notes...", which caught on. Videos focus on frequent topics in therapy, with useful insights and skills for the general public.
Medical
Anyone interested in personal growth. All ages but probably young adults who are more comfortable with technology. My goal is to create a following that can be monetized at some point.
I want my banner to be bright, professional, and friendly. I like a clean, modern feel. While I use a self-made logo, I'm not very happy with it, so please feel free to be creative and come up with something new! My current YouTube channel: https://www.vidloop.example/@LiviaNotes

```html
<!DOCTYPE html>
<html lang="en">
<head>
<meta charset="UTF-8">
<title>Livia Notes – Psychology Insights Banner</title>
<link rel="stylesheet" href="https://fonts.googleapis.com/css2?family=Poppins:wght@500;700;800&display=swap">
<style>
  :root {
    --bg-light: #f1ebf8;
    --bg-mid: #e3d6f1;
    --bg-wave: #d9c8ee;
    --violet: #8a55e8;
    --violet-deep: #6f3fd1;
    --plum: #a33fb8;
    --yellow: #f6e04e;
    --yellow-shadow: #c9a82a;
    --ink: #4a2f7a;
    --pill-line: #8f6fcf;
    --white: #ffffff;
  }
  * { margin: 0; padding: 0; box-sizing: border-box; }
  html, body { width: 1200px; height: 674px; overflow: hidden; background: var(--bg-light); }
  .banner {
    position: relative;
    width: 1200px;
    height: 674px;
    overflow: hidden;
    background: linear-gradient(120deg, var(--bg-light) 0%, var(--bg-mid) 60%, var(--bg-wave) 100%);
    font-family: "Poppins", sans-serif;
  }
  .backdrop-waves, .accent-shape { position: absolute; inset: 0; width: 1200px; height: 674px; }
  .brain-art {
    position: absolute;
    left: 290px; top: 120px;
    width: 320px; height: 300px;
    border-radius: 48% 52% 46% 54%;
    background: radial-gradient(circle at 50% 45%, rgba(190,170,225,0.55), rgba(220,205,240,0) 70%);
  }
  .brand {
    position: absolute;
    left: 200px; top: 62px;
    display: flex; align-items: center; gap: 16px;
  }
  .brand-dot {
    width: 34px; height: 34px; border-radius: 50%;
    background: var(--plum);
  }
  .brand-name {
    font-weight: 800;
    font-size: 52px;
    line-height: 1;
    color: var(--plum);
    letter-spacing: 0.5px;
  }
  .headline {
    position: absolute;
    left: 96px; top: 160px;
    font-weight: 800;
    font-size: 104px;
    line-height: 112px;
    color: var(--yellow);
    text-shadow: 3px 4px 0 var(--yellow-shadow);
    letter-spacing: -1px;
  }
  .host-pill {
    position: absolute;
    left: 163px; top: 542px;
    width: 394px; height: 62px;
    border: 3px solid var(--pill-line);
    border-radius: 31px;
    display: flex; align-items: center;
    padding-left: 24px; gap: 22px;
    background: rgba(255,255,255,0.25);
  }
  .host-pill svg { flex: none; }
  .host-name {
    font-weight: 500;
    font-size: 27px;
    color: var(--ink);
  }
  .host-photo {
    position: absolute;
    left: 700px; top: 14px;
    width: 360px; height: 660px;
    border-radius: 180px 180px 0 0;
    background: linear-gradient(180deg, #8a6a52 0%, #d9b49a 35%, #2b2b30 65%, #1d1d22 100%);
  }
</style>
</head>
<body>
  <main class="banner">
    <svg class="backdrop-waves" viewBox="0 0 1200 674" aria-hidden="true">
      <path d="M0 360 C 220 300 380 420 620 360 S 900 300 1200 340 L1200 674 L0 674 Z" fill="#ebe1f6" opacity="0.7"/>
      <path d="M0 520 C 260 470 420 580 700 520 L700 674 L0 674 Z" fill="#e6daf3" opacity="0.8"/>
    </svg>

    <div class="brain-art" role="img" aria-label="Faint brain illustration behind the headline"></div>

    <svg class="accent-shape" viewBox="0 0 1200 674" aria-hidden="true">
      <path d="M800 0 L1200 0 L1200 674 L640 674 C 650 600 700 560 690 480 C 680 400 640 360 660 280 C 690 170 830 150 860 80 C 875 45 840 20 800 0 Z" fill="var(--violet)"/>
      <path d="M1060 0 L1200 0 L1200 210 C 1140 180 1080 120 1060 0 Z" fill="var(--violet-deep)" opacity="0.5"/>
      <circle cx="744" cy="336" r="108" fill="var(--yellow)" opacity="0.9"/>
    </svg>

    <div class="host-photo" role="img" aria-label="Portrait photo of Dr. Livia Torrent smiling, in a dark blazer"></div>

    <div class="brand">
      <span class="brand-dot"></span>
      <span class="brand-name">Livia Notes</span>
    </div>

    <h1 class="headline">Psychology<br>Insights<br>with</h1>

    <div class="host-pill">
      <svg width="26" height="28" viewBox="0 0 26 28" aria-hidden="true">
        <path d="M3 2 L24 14 L3 26 Z" fill="none" stroke="var(--ink)" stroke-width="3" stroke-linejoin="round"/>
      </svg>
      <span class="host-name">Dr. Livia Torrent</span>
    </div>
  </main>
</body>
</html>
```